Web Design Project

Hi everyone

Thanks for taking the time to read about this project.

Website needed for Corvel, female singer/songwriter and performer who is launching her debut album this year. She writes and performs folk/pop/soft rock music and plays guitar and piano.

see vidrelay links for examples of Corvel's style:
http://www.vidrelay.example/watch?v=Qp3TzL8wRn2
http://www.vidrelay.example/watch?v=Hk7DbVu4sYe

Looking for a classy, modern feel to the website. Cool colours are preferred but open to ideas. It needs it to have CoinTrove set up so items can be purchased from the site. The theme will be continued to Friendspace and business cards.

Examples include:

http://www.belindacrosshaw.example/

http://tessavorlund.example/

http://www.juneqtunes.example/home

Pages and content to be included:

HOME - main picture and general content

BIO - written content about Corvel

NEWS - this will be regularly updated, blog style

GIGS - this will be regularly updated

GALLERY - content will be photos only

SEE AND HEAR - content will be Videos and audios

STORE - this will have a cointrove function for purchase of CD and merchandise

GENEROSITY - this page will be devoted to charity work and updated regularly

CONTACT - information on how to contact Corvel's management

Buttons will need to provide links to VidRelay, Chirpline, Friendspace, Snapwell

I will work closely with the designers in giving feedback as ideas are generated and then provide further content such as photos and videos.

Thanks for considering this project!
Updates

HI everyone thanks for all your submissions so far. Please note the following:

- photos have been uploaded to assist with themes

- background could be a solid colour or texture (e.g. tree trunk texture)

- please use a hand writing font similar to Fontaro font "Lift Our Voice" - doesn't have to be exactly this but similar

Thank you,

Corvel

Hi again everyone

I apologise but the pixel bazaar website won't allow me to upload files. I will attempt to correct this as soon as possible. Thanks                                   

Target Market(s)

18-55 year olds who appreciate this genre of music; gay and lesbian community

Industry/Entity Type

Charity

Requirements
Should not have
• No flowers or flowery themes

```html
<!DOCTYPE html>
<html lang="en">
<head>
<meta charset="utf-8">
<title>Corvel — Official Website</title>
<link rel="stylesheet" href="https://fonts.googleapis.com/css2?family=Dancing+Script:wght@500&family=Lora:ital,wght@1,400;1,700&family=Open+Sans:wght@400;600&display=swap">
<style>
  :root {
    --ink-dark: #1c1c1e;
    --header-top: #3a3c40;
    --header-bottom: #1f2023;
    --nav-bg: #f4f4f4;
    --nav-text: #3b3b3b;
    --accent-blue: #2f7fc8;
    --accent-blue-dark: #1d5f9e;
    --paper: #e9ebea;
    --paper-deep: #d6dad9;
    --card-bg: #f7f8f7;
    --card-border: #c9cdcc;
    --body-text: #3a3a3a;
    --band-dark: #2a2a2b;
    --footer-bg: #161617;
    --muted: #9a9a9a;
    --white: #ffffff;
  }
  * { box-sizing: border-box; margin: 0; padding: 0; }
  html, body { width: 800px; height: 1200px; overflow: hidden; }
  body {
    position: relative;
    background: var(--paper);
    font-family: "Open Sans", Arial, sans-serif;
    color: var(--body-text);
  }

  /* Header */
  .site-header {
    position: absolute; left: 0; top: 0; width: 800px; height: 80px;
    background: linear-gradient(var(--header-top), var(--header-bottom));
  }
  .logo {
    position: absolute; left: 30px; top: 4px;
    font-family: "Dancing Script", cursive;
    font-size: 42px; color: var(--accent-blue); font-weight: 500;
  }
  .social {
    position: absolute; right: 26px; top: 12px;
    display: flex; gap: 14px; list-style: none;
    font-size: 11px; font-weight: 600; color: var(--white);
  }
  .social li { display: flex; align-items: center; gap: 5px; }
  .social .dot { width: 12px; height: 12px; background: var(--accent-blue); }
  .main-nav {
    position: absolute; right: 6px; top: 44px; height: 26px;
    background: var(--nav-bg); border-radius: 4px;
    display: flex; align-items: center; padding: 0 10px; gap: 16px;
    list-style: none; font-size: 11px; color: var(--nav-text);
  }
  .main-nav .active {
    background: var(--accent-blue); color: var(--white);
    padding: 3px 8px; border-radius: 3px;
  }

  /* Hero */
  .hero {
    position: absolute; left: 0; top: 80px; width: 800px; height: 425px;
    background: radial-gradient(ellipse at 55% 40%, #8a6a4e 0%, #4a3a2e 30%, #1e1b19 65%, #0f0e0e 100%);
  }
  .hero-arrow { position: absolute; top: 190px; }
  .hero-arrow.prev { left: 12px; }
  .hero-arrow.next { right: 12px; }
  .hero-caption {
    position: absolute; left: 0; bottom: 0; width: 800px; height: 110px;
    background: linear-gradient(rgba(0,0,0,0.35), rgba(0,0,0,0.75));
    padding: 10px 36px; color: var(--white);
  }
  .hero-caption .kicker { font-family: "Lora", serif; font-style: italic; font-size: 13px; }
  .hero-caption h1 {
    font-family: "Lora", serif; font-style: italic; font-weight: 400;
    font-size: 26px; margin: 2px 0 6px;
  }
  .hero-caption h1 span { color: var(--accent-blue); }
  .hero-caption p {
    font-family: "Lora", serif; font-style: italic; font-size: 12px;
    line-height: 1.4; width: 560px; color: #e6e6e6;
  }

  /* Feature cards */
  .features {
    position: absolute; left: 0; top: 505px; width: 800px; height: 340px;
    background: linear-gradient(var(--paper), var(--paper-deep));
  }
  .card {
    position: absolute; top: 30px; width: 213px; height: 280px;
    background: var(--card-bg); border: 1px solid var(--card-border);
    box-shadow: 0 2px 6px rgba(0,0,0,0.15);
  }
  .card:nth-child(1) { left: 40px; }
  .card:nth-child(2) { left: 293px; }
  .card:nth-child(3) { left: 547px; }
  .ribbon {
    position: absolute; left: -8px; top: -12px; width: 26px; height: 50px;
    background: var(--accent-blue);
    box-shadow: 1px 1px 3px rgba(0,0,0,0.25);
  }
  .ribbon::before {
    content: ""; position: absolute; left: 0; top: -6px;
    border-style: solid; border-width: 0 0 6px 8px;
    border-color: transparent transparent var(--accent-blue-dark) transparent;
  }
  .ribbon-label {
    position: absolute; left: 4px; top: 52px; width: 30px; height: 196px;
    writing-mode: vertical-rl; transform: rotate(180deg);
    text-align: left;
    font-family: "Lora", serif; font-style: italic; font-size: 21px; line-height: 30px;
    color: var(--accent-blue); white-space: nowrap;
  }
  .card-photo {
    position: absolute; left: 40px; top: 28px; width: 160px; height: 110px;
    background: linear-gradient(135deg, #6b5440, #2b2320);
    border: 2px solid var(--white);
  }
  .card-text {
    position: absolute; left: 40px; top: 150px; width: 162px;
    font-size: 9.5px; line-height: 1.45;
  }
  .more-btn {
    position: absolute; left: 40px; bottom: 24px;
    background: var(--band-dark); color: var(--white);
    font-size: 10px; padding: 4px 12px; border-radius: 2px;
  }

  /* Latest update */
  .section-title {
    position: absolute; left: 40px; top: 846px;
    font-family: "Lora", serif; font-style: italic; font-weight: 700;
    font-size: 24px; color: var(--ink-dark);
  }
  .updates {
    position: absolute; left: 0; top: 882px; width: 800px; height: 268px;
    background: var(--band-dark);
  }
  .video-player {
    position: absolute; left: 40px; top: 12px; width: 350px; height: 205px;
    background: linear-gradient(135deg, #5a4636, #1e1a18);
    border: 2px solid #444;
  }
  .video-controls {
    position: absolute; left: 0; bottom: 0; width: 100%; height: 20px;
    background: rgba(0,0,0,0.7);
  }
  .video-controls .bar {
    position: absolute; left: 30px; right: 60px; top: 9px; height: 3px; background: #666;
  }
  .video-controls .bar::after {
    content: ""; position: absolute; left: 0; top: 0; width: 30%; height: 3px; background: var(--accent-blue);
  }
  .now-playing {
    position: absolute; left: 40px; top: 228px;
    font-family: "Lora", serif; font-style: italic; font-size: 13px; color: var(--white);
  }
  .playlist {
    position: absolute; left: 525px; top: 10px; width: 140px; text-align: center;
  }
  .playlist-thumb {
    width: 130px; height: 100px; margin: 10px auto 6px;
    background: linear-gradient(135deg, #5e4a3a, #221d1a);
    border: 3px solid var(--white);
  }
  .playlist-link { font-size: 10px; color: var(--accent-blue); text-decoration: underline; }

  /* Footer */
  .site-footer {
    position: absolute; left: 0; top: 1150px; width: 800px; height: 50px;
    background: var(--footer-bg); color: var(--muted); font-size: 9px;
  }
  .footer-links { position: absolute; left: 40px; top: 20px; }
  .footer-social {
    position: absolute; left: 300px; top: 16px; display: flex; gap: 12px;
    list-style: none; font-size: 11px; font-weight: 600; color: var(--white);
  }
  .footer-social li { display: flex; align-items: center; gap: 5px; }
  .footer-social .dot { width: 11px; height: 11px; background: var(--accent-blue); }
  .copyright { position: absolute; right: 36px; top: 20px; }
</style>
</head>
<body>

<header class="site-header">
  <div class="logo">Corvel</div>
  <ul class="social">
    <li><span class="dot"></span>Friendspace</li>
    <li><span class="dot"></span>Chirpline</li>
    <li><span class="dot"></span>VidRelay</li>
  </ul>
  <ul class="main-nav">
    <li class="active">Home</li>
    <li>Bio</li>
    <li>News</li>
    <li>Gigs</li>
    <li>Gallery</li>
    <li>See &amp; Hear</li>
    <li>Store</li>
    <li>Generosity</li>
    <li>Contact</li>
  </ul>
</header>

<section class="hero" role="img" aria-label="Portrait photograph of singer Corvel on stage">
  <svg class="hero-arrow prev" width="20" height="40" viewBox="0 0 20 40"><path d="M16 4 L4 20 L16 36" fill="none" stroke="rgba(255,255,255,0.35)" stroke-width="3"/></svg>
  <svg class="hero-arrow next" width="20" height="40" viewBox="0 0 20 40"><path d="M4 4 L16 20 L4 36" fill="none" stroke="rgba(255,255,255,0.35)" stroke-width="3"/></svg>
  <div class="hero-caption">
    <div class="kicker">Welcome to</div>
    <h1>Official Website of <span>Corvel</span></h1>
    <p>Female singer / Songwriter and Performer who is launching her debut album this year. She writes and performs folk... pop... soft... rock music and plays guitar and piano.</p>
  </div>
</section>

<section class="features">
  <article class="card">
    <div class="ribbon"></div>
    <div class="ribbon-label">Store</div>
    <div class="card-photo" role="img" aria-label="Photo of Corvel for the store"></div>
    <p class="card-text">Our development services related to soft-ware are known for implementing the best practices in the industry.</p>
    <span class="more-btn">More...</span>
  </article>
  <article class="card">
    <div class="ribbon"></div>
    <div class="ribbon-label">See &amp; Hear</div>
    <div class="card-photo" role="img" aria-label="Photo of Corvel for videos and audio"></div>
    <p class="card-text">Our development services related to soft-ware are known for implementing the best practices in the industry.</p>
    <span class="more-btn">More...</span>
  </article>
  <article class="card">
    <div class="ribbon"></div>
    <div class="ribbon-label">Gallery</div>
    <div class="card-photo" role="img" aria-label="Photo of Corvel for the gallery"></div>
    <p class="card-text">Our development services related to soft-ware are known for implementing the best practices in the industry.</p>
    <span class="more-btn">More...</span>
  </article>
</section>

<h2 class="section-title">Latest Update</h2>

<section class="updates">
  <div class="video-player" role="img" aria-label="Video still of Corvel playing acoustic guitar">
    <div class="video-controls"><div class="bar"></div></div>
  </div>
  <p class="now-playing">Now Playing - Corvel Ashdown - Quiet Harbour (cover)</p>
  <div class="playlist">
    <svg width="30" height="16" viewBox="0 0 30 16"><path d="M3 14 L15 3 L27 14" fill="none" stroke="#777" stroke-width="4"/></svg>
    <div class="playlist-thumb" role="img" aria-label="Thumbnail of Corvel performing with guitar"></div>
    <div class="playlist-link">See this video</div>
    <svg width="30" height="16" viewBox="0 0 30 16" style="margin-top:14px"><path d="M3 2 L15 13 L27 2" fill="none" stroke="#777" stroke-width="4"/></svg>
  </div>
</section>

<footer class="site-footer">
  <div class="footer-links">About Us | Privacy Policy | Terms And Condition</div>
  <ul class="footer-social">
    <li><span class="dot"></span>Friendspace</li>
    <li><span class="dot"></span>Chirpline</li>
    <li><span class="dot"></span>VidRelay</li>
  </ul>
  <div class="copyright">Copyright 2013 &copy;. All Rights Reserved.</div>
</footer>

</body>
</html>
```